Velmora Harbor Church Direct Mail Postcard

We are launching a new church in Olathe Kansas (Kansas City suburb). People here are well educated and pretty affluent. There are many young families which is our mail target demo. We need a 6 inch by 11 inch postcard that will be for a mass mailer that will coincide with our launch. The goal is simply to get people to come to the church launch which is September 18th. We think the theme should be "What in Heaven are you here for?" or "God is not Mad at you..No Matter What?" or "The truth is...you matter." It needs to include a map to our church which is inside Copper Ridge Middle School: 18400 W 93rd St, Olathe, KS 66047. Service is at 10:00 am, Safe childcare is provided from infants up to 12 year olds. There should be some space for us to put in some messaging and bullets. Possibly include a few pictures of happy families and people worshiping. I’ve attached our Logo, but we actually need to flip the colors so that the blue arrow is on top and pointing down, and the gray arrow is pointing up.

Target Market(s)

Young Families

Industry/Entity Type

Church

Requirements
Must have
• Post Card should be front and back full color
• Our website clearly shown on the back: VelmoraHarborChurch.com
• There should be a small map on the back with our location.
• It should say our service starts at 10:00 and that we our first service is Sept 18th
• The message or images on the front are there primarily to get people to turn the card over. UPDATE: We like the idea "What in Heaven are you here for?" on the front the best, followed by "God is NOT Mad at you..." (front) "no matter what" (back) second, and then "The truth is.." (front) "You matter" back third.
• Only 1 of the themes should be used at a time. So for example, the front should say, "What In Heaven are you here for?" or "God is not mad at you..." but not both.
• We like clean, modern looks. Don't put the logo on the front.
Nice to have
• Some stock photos of families or people worshipping (contemporary charismatic church)
• I attached some examples of cards that worked well for other churches. Please check them out.
Should not have
• The words "Grand Opening"

```html
<!DOCTYPE html>
<html lang="en">
<head>
<meta charset="utf-8">
<title>Velmora Harbor Church – Launch Postcard</title>
<link rel="stylesheet" href="https://fonts.googleapis.com/css2?family=Josefin+Sans:wght@300&family=Poiret+One&family=Oswald:wght@300;400&family=Open+Sans:wght@400;600&display=swap">
<style>
  :root {
    --stage: #e9e6e1;
    --board: #1f1f1f;
    --board-light: #2c2c2c;
    --ink: #ffffff;
    --sky: #5aa9e6;
    --navy: #2b4f9e;
    --grey: #666666;
    --paper: #ffffff;
    --body-ink: #333333;
  }
  * { margin: 0; padding: 0; box-sizing: border-box; }
  html, body { width: 1200px; height: 1071px; overflow: hidden; background: var(--stage); }
  .canvas { position: relative; width: 1200px; height: 1071px; }

  /* ---------- front ---------- */
  .card-front {
    position: absolute; left: 63px; top: 53px; width: 515px; height: 942px;
    background: radial-gradient(ellipse at 45% 40%, var(--board-light) 0%, var(--board) 70%);
    color: var(--ink);
    font-family: "Josefin Sans", "Century Gothic", sans-serif;
    font-weight: 300;
    text-align: center;
  }
  .headline { position: absolute; left: 0; right: 0; top: 168px; line-height: 1; }
  .headline span { display: block; }
  .headline .big { font-size: 104px; letter-spacing: 2px; height: 118px; }
  .headline .small { font-size: 48px; height: 52px; letter-spacing: 2px; }
  .headline .accent { color: var(--sky); }
  .front-name {
    position: absolute; left: 0; right: 0; top: 732px;
    font-size: 20px; letter-spacing: 3px; text-transform: uppercase; color: var(--ink);
  }

  /* ---------- back ---------- */
  .card-back {
    position: absolute; left: 629px; top: 53px; width: 514px; height: 942px;
    background: var(--paper); overflow: hidden;
  }
  .back-upper { position: absolute; left: 0; top: 0; width: 514px; height: 515px; background: var(--board); }
  .back-map-column { position: absolute; left: 258px; top: 515px; width: 256px; height: 264px; background: var(--board); }
  .back-title {
    position: absolute; left: 117px; top: 58px;
    font-family: "Poiret One", "Century Gothic", sans-serif;
    font-size: 48px; line-height: 48px; color: var(--ink); letter-spacing: 3px;
  }
  .launch { position: absolute; left: 22px; top: 260px; color: var(--ink); }
  .launch-line {
    font-family: "Oswald", sans-serif; font-weight: 300; font-size: 21px;
    line-height: 24px; text-transform: uppercase; transform: scaleX(.82); transform-origin: left;
    white-space: nowrap;
  }
  .launch-line .accent { color: var(--sky); }
  .launch-date {
    font-family: "Open Sans", sans-serif; font-weight: 600; font-size: 13.5px;
    letter-spacing: 1.2px; color: var(--sky); margin: 0 0 6px;
  }
  .photo-strip { position: absolute; left: 0; top: 335px; width: 514px; height: 105px; display: flex; }
  .photo { height: 100%; }
  .photo-a { width: 162px; background: linear-gradient(160deg, #8a8a8a, #3a3a3a); }
  .photo-b { width: 160px; background: linear-gradient(200deg, #a5a5a5, #555); }
  .photo-c { width: 192px; background: linear-gradient(150deg, #5c5c5c, #b0b0b0 60%, #4a4a4a); }
  .invite { position: absolute; left: 22px; top: 444px; font-family: "Open Sans", sans-serif; }
  .invite h2 { font-weight: 400; font-size: 14px; color: var(--sky); letter-spacing: .6px; margin-bottom: 5px; }
  .invite ul { list-style: none; }
  .invite li { font-size: 11.5px; line-height: 12.5px; color: var(--ink); letter-spacing: .3px; }
  .invite li::before { content: "➤"; color: var(--sky); font-size: 8px; margin-right: 5px; vertical-align: 1px; }
  .map {
    position: absolute; left: 279px; top: 517px; width: 214px; height: 230px;
    background: linear-gradient(180deg, #ecebe6 0%, #e3dcc3 60%, #d9cfa8 100%);
  }
  .map-label {
    position: absolute; left: 395px; top: 575px;
    font-family: "Open Sans", sans-serif; font-weight: 600; font-size: 11.5px; line-height: 13px; color: #b3221c;
  }
  .map-pin { position: absolute; left: 374px; top: 551px; }
  .return-address {
    position: absolute; left: 238px; top: 722px; width: 112px;
    transform: rotate(90deg); transform-origin: 0 0;
    font-family: "Oswald", sans-serif; font-weight: 400; font-size: 10px; line-height: 12px; color: var(--body-ink);
    text-transform: none; white-space: nowrap;
  }
  .return-address .org { text-transform: uppercase; }
  .stamp-box { position: absolute; left: 172px; top: 850px; width: 68px; height: 67px; border: 2px dashed #aaa; }
  .sign-off { position: absolute; left: 264px; top: 794px; }
  .sign-off .name {
    font-family: "Oswald", sans-serif; font-weight: 400; font-size: 23px; line-height: 26px;
    color: var(--navy); text-transform: uppercase; letter-spacing: -.3px; white-space: nowrap;
  }
  .sign-off .tagline { font-family: "Open Sans", sans-serif; font-size: 13px; color: var(--grey); margin-left: 65px; margin-top: -2px; }
  .contact { position: absolute; left: 270px; top: 841px; list-style: none; font-family: "Open Sans", sans-serif; font-size: 13px; line-height: 16.8px; color: var(--body-ink); }
  .contact li { display: flex; align-items: center; gap: 6px; }
  .contact svg { width: 13px; height: 13px; flex: none; }
  .contact .indent { padding-left: 19px; }
</style>
</head>
<body>
<main class="canvas">

  <section class="card-front" aria-label="Postcard front">
    <h1 class="headline">
      <span class="big">GOD</span>
      <span class="small accent">IS</span>
      <span class="big accent">NOT</span>
      <span class="big">MAD</span>
      <span class="small">AT</span>
      <span class="big">YOU</span>
    </h1>
    <p class="front-name">Velmora Harbor Church</p>
  </section>

  <section class="card-back" aria-label="Postcard back">
    <div class="back-upper"></div>
    <div class="back-map-column"></div>

    <h2 class="back-title">NO MATTER<br>WHAT</h2>

    <div class="launch">
      <p class="launch-line">Velmora Harbor Church <span class="accent">is about to take off</span></p>
      <p class="launch-date">SEPTEMBER 18, 2016 | 10:00 AM</p>
      <p class="launch-line">You are invited to join the fun!</p>
    </div>

    <div class="photo-strip">
      <div class="photo photo-a" role="img" aria-label="Black and white photo of a congregation worshipping with raised hands"></div>
      <div class="photo photo-b" role="img" aria-label="Black and white photo of people singing during worship"></div>
      <div class="photo photo-c" role="img" aria-label="Black and white photo of a crowd with hands lifted in praise"></div>
    </div>

    <div class="invite">
      <h2>Bring Your Family and Join Us!</h2>
      <ul>
        <li>Connect with people who accept you for who you are</li>
        <li>A safe place for kids to learn and grow in fun, creative ways</li>
        <li>Experience exciting worship in a casual, relaxed atmosphere</li>
      </ul>
    </div>

    <div class="map" role="img" aria-label="Street map showing the church location at Copper Ridge Middle School, 18400 W 93rd St, Olathe, KS 66047"></div>
    <svg class="map-pin" width="20" height="30" viewBox="0 0 20 30" aria-hidden="true">
      <path d="M10 29 C10 29 1 16 1 10 A9 9 0 0 1 19 10 C19 16 10 29 10 29Z" fill="#e0352b"/>
      <circle cx="10" cy="10" r="3.2" fill="#8b1510"/>
    </svg>
    <p class="map-label">Copper Ridge<br>Middle School</p>

    <p class="return-address"><span class="org">Velmora Harbor Church</span><br>P.O. Box 4408<br>Shawnee, KS 66218</p>
    <div class="stamp-box"></div>

    <div class="sign-off">
      <p class="name">Velmora Harbor Church</p>
      <p class="tagline">Love · Wisdom · Power</p>
    </div>

    <ul class="contact">
      <li><svg viewBox="0 0 14 14"><rect x="1" y="3" width="12" height="8" fill="none" stroke="#333"/><path d="M1 3 L7 8 L13 3" fill="none" stroke="#333"/></svg>info@vhc.church</li>
      <li><svg viewBox="0 0 14 14"><path d="M3 1 L5 1 L6 4 L4.5 5 Q6 8.5 9 9.5 L10 8 L13 9 L13 11 Q12 13 10 13 Q3 11 1 4 Q1 2 3 1Z" fill="none" stroke="#333"/></svg>913.555.0142</li>
      <li><svg viewBox="0 0 14 14"><rect x="1" y="3" width="12" height="8" fill="none" stroke="#333"/><path d="M1 3 L7 8 L13 3" fill="none" stroke="#333"/></svg>P.O. Box 4408</li>
      <li class="indent">Shawnee, KS 66218</li>
      <li><svg viewBox="0 0 14 14"><circle cx="7" cy="7" r="6" fill="none" stroke="#333"/><ellipse cx="7" cy="7" rx="2.5" ry="6" fill="none" stroke="#333"/><path d="M1 7 H13" stroke="#333"/></svg>velmoraharborchurch.com</li>
    </ul>
  </section>

</main>
</body>
</html>
```